Project Manager Business Card for Top Architectural Firm

Update and design a stunning Senior Project Manager Business Card

MARCO T. RUEDA II
Senior Project Manager

H A R B O R L I N E
A R C H I T E C T U R E L L C.
www.HarborlineCrestHouses.com
4217 NW 38th Ter. Suite 905
Miami, FL 33172
C: (305) 418-2273
mrueda.harborlinecresthouses@mailvista.net

Looking to have the logo to be UV Spot ink printed and to be prominent.

Target Market(s)

High end real estate architecture construction

Industry/Entity Type

Architect

Contact Information for Business Card

MARCO T. RUEDA II
Senior Project Manager

H A R B O R L I N E
Miami, FL 33172
C: (305) 418-2273

Font styles to use
Sans Serif

Colors

Designer to choose colors to be used in the design.

Requirements
Must have
• Prominent Logo

```html
<!DOCTYPE html>
<html lang="en">
<head>
<meta charset="utf-8">
<title>Harborline Architecture LLC – Business Card</title>
<link href="https://fonts.googleapis.com/css2?family=Open+Sans:wght@300;400;600;700&display=swap" rel="stylesheet">
<style>
  :root {
    --stage: #e4e6e8;
    --card-black: #050505;
    --sky: #49ade0;
    --sky-light: #7fcaee;
    --sky-deep: #2f8fc8;
    --accent-blue: #3aa6e0;
    --accent-red: #e8553a;
    --ink-white: #ffffff;
    --ink-soft: #e9e9e9;
  }
  * { margin: 0; padding: 0; box-sizing: border-box; }
  html, body { width: 1200px; height: 782px; overflow: hidden; }
  body {
    background: var(--stage);
    font-family: "Open Sans", Arial, sans-serif;
    position: relative;
  }
  .card {
    position: absolute;
    top: 236px;
    width: 540px;
    height: 309px;
    border-radius: 3px;
    overflow: hidden;
    box-shadow: 0 6px 18px rgba(0,0,0,0.18);
  }
  /* Front */
  .card-front {
    left: 40px;
    background: linear-gradient(125deg, var(--sky-deep) 0%, var(--sky) 45%, var(--sky-light) 100%);
  }
  .front-wordmark {
    position: absolute;
    left: 0; right: 0; top: 112px;
    text-align: center;
    color: var(--ink-white);
    font-weight: 300;
  }
  .front-wordmark .name {
    display: block;
    font-size: 52px;
    letter-spacing: 10px;
    line-height: 1;
  }
  .front-wordmark .suffix {
    display: block;
    margin-top: 10px;
    font-size: 15px;
    letter-spacing: 7px;
  }
  /* Back */
  .card-back {
    left: 620px;
    background: var(--card-black);
  }
  .back-logo {
    position: absolute;
    left: 22px;
    top: 104px;
    width: 200px;
    color: var(--ink-white);
    font-weight: 300;
    text-align: center;
  }
  .back-logo .mark-dot {
    display: block;
    width: 44px; height: 44px;
    margin: 0 auto 14px;
    border-radius: 50%;
    background: var(--accent-blue);
  }
  .back-logo .name {
    display: block;
    font-size: 24px;
    letter-spacing: 4px;
    line-height: 1;
  }
  .back-logo .suffix {
    display: block;
    margin-top: 6px;
    font-size: 8.5px;
    letter-spacing: 3px;
  }
  .contact {
    position: absolute;
    left: 248px;
    top: 62px;
    color: var(--ink-white);
    font-size: 12px;
    line-height: 1.38;
  }
  .contact .person {
    color: var(--accent-blue);
    font-weight: 700;
    font-size: 16px;
    line-height: 1.1;
  }
  .contact .role {
    color: var(--accent-red);
    font-weight: 600;
    font-size: 12.5px;
    margin-bottom: 4px;
  }
  .contact .firm {
    letter-spacing: 1.5px;
    color: var(--ink-soft);
  }
  .contact .line { display: flex; align-items: center; gap: 6px; }
  .contact .line svg { width: 11px; height: 11px; flex: none; fill: var(--accent-blue); }
  .contact .email { font-size: 10.8px; }
</style>
</head>
<body>

<section class="card card-front" aria-label="Card front">
  <div class="front-wordmark">
    <span class="name">HARBORLINE</span>
    <span class="suffix">ARCHITECTURE LLC</span>
  </div>
</section>

<section class="card card-back" aria-label="Card back">
  <div class="back-logo">
    <span class="mark-dot"></span>
    <span class="name">HARBORLINE</span>
    <span class="suffix">ARCHITECTURE LLC</span>
  </div>

  <div class="contact">
    <p class="person">MARCO T. RUEDA II</p>
    <p class="role">Senior Project Manager</p>
    <p class="firm">H A R B O R L I N E<br>A R C H I T E C T U R E L L C.</p>
    <p>4217 NW 38th Ter. Suite 905</p>
    <p>Miami, FL 33172</p>
    <p class="line">
      <svg viewBox="0 0 24 24" aria-hidden="true"><path d="M6.6 10.8a15.1 15.1 0 0 0 6.6 6.6l2.2-2.2a1 1 0 0 1 1-.25 11.4 11.4 0 0 0 3.6.57 1 1 0 0 1 1 1V20a1 1 0 0 1-1 1A17 17 0 0 1 3 4a1 1 0 0 1 1-1h3.5a1 1 0 0 1 1 1c0 1.25.2 2.45.57 3.57a1 1 0 0 1-.25 1z"/></svg>
      (305) 418-2273
    </p>
    <p class="line">
      <svg viewBox="0 0 24 24" aria-hidden="true"><path d="M12 2a10 10 0 1 0 0 20 10 10 0 0 0 0-20zm6.9 6h-2.9a15.7 15.7 0 0 0-1.4-3.6A8 8 0 0 1 18.9 8zM12 4c.8 1.2 1.5 2.5 1.9 4h-3.8c.4-1.5 1.1-2.8 1.9-4zM4.3 14a8 8 0 0 1 0-4h3.4a16.5 16.5 0 0 0 0 4zm.8 2h2.9c.3 1.3.8 2.5 1.4 3.6A8 8 0 0 1 5.1 16zM8 8H5.1a8 8 0 0 1 4.3-3.6C8.8 5.5 8.3 6.7 8 8zm4 12c-.8-1.2-1.5-2.5-1.9-4h3.8c-.4 1.5-1.1 2.8-1.9 4zm2.3-6H9.7a14.7 14.7 0 0 1 0-4h4.6a14.7 14.7 0 0 1 0 4zm.3 5.6c.6-1.1 1.1-2.3 1.4-3.6h2.9a8 8 0 0 1-4.3 3.6zm1.7-5.6a16.5 16.5 0 0 0 0-4h3.4a8 8 0 0 1 0 4z"/></svg>
      www.HarborlineCrestHouses.com
    </p>
    <p class="line email">
      <svg viewBox="0 0 24 24" aria-hidden="true"><path d="M3 5h18a1 1 0 0 1 1 1v12a1 1 0 0 1-1 1H3a1 1 0 0 1-1-1V6a1 1 0 0 1 1-1zm9 7.2L4.4 7H19.6zM4 9v8h16V9l-8 5.4z"/></svg>
      mrueda.harborlinecresthouses@mailvista.net
    </p>
  </div>
</section>

</body>
</html>
```